The Merry Hound - Dog Training Business Card Design

I need a business card design for a new dog training company based in Cronulla NSW called The Merry Hound. I run puppy pre school classes, adult dog classes and do one on one training in the person's home.
I have studied for 2 years and use positive reinforcement training methods based on how dogs learn. I believe in communicating with our dogs what we want them to do rather than punish them for behaviours we don't like. I would like to see designs that use the colours that are used in my logo (please see attached)
I would like a simple and classic looking design. I don't want cartoon images of dogs or any animal images or drawings on the card. I have created my logo with this mindset. I am open to the subtle use of a dog's tail, paws or paw print.

Target Market(s)

high end area which is why I want a classic looking design
adults aged 25 and over

Industry/Entity Type

Dog Training

Contact Information for Business Card

Miriam Caslett
ORBIS Trained Professional Dog Trainer
www.themerryhound-example.com.au
0499731628
miriam@themerryhound-example.com.au

Font styles to use
Sans Serif

Colors
ffffff
86cae6
757575

Requirements
Must have
• Logo - I am trying to attach my logo and colour palette but it won't allow me. I will contact the company and upload ASAP.
Should not have
• images of dogs or cartoon drawings

```html
<!DOCTYPE html>
<html lang="en">
<head>
<meta charset="utf-8">
<title>The Merry Hound – Business Card</title>
<link rel="stylesheet" href="https://fonts.googleapis.com/css2?family=Open+Sans:wght@300;400;600&display=swap">
<style>
  :root {
    --white: #ffffff;
    --sky: #86cae6;
    --sky-soft: #a9cbe6;
    --slate: #757575;
    --slate-dark: #5a5f61;
    --ink: #4a4d4f;
    --backdrop: #eceeef;
    --font: "Open Sans", Arial, sans-serif;
  }
  * { box-sizing: border-box; margin: 0; padding: 0; }
  html, body { width: 1200px; height: 800px; overflow: hidden; }
  body {
    background: var(--backdrop);
    font-family: var(--font);
    display: flex;
    align-items: center;
    justify-content: center;
    gap: 60px;
  }
  .card {
    position: relative;
    width: 525px;
    height: 300px;
    overflow: hidden;
    box-shadow: 0 6px 18px rgba(0,0,0,0.12);
  }
  .card-front { background: var(--sky-soft); }
  .card-front .sweep { position: absolute; inset: 0; width: 100%; height: 100%; }
  .front-content { position: absolute; left: 34px; top: 30px; right: 160px; }
  .brand { display: flex; align-items: center; gap: 10px; }
  .brand-name {
    font-weight: 300;
    font-size: 34px;
    line-height: 1;
    color: var(--slate);
    letter-spacing: -0.5px;
    white-space: nowrap;
  }
  .brand-dot {
    width: 22px; height: 22px;
    border-radius: 50%;
    background: var(--sky);
    flex: none;
  }
  .tagline {
    margin-top: 8px;
    font-size: 9px;
    letter-spacing: 2.2px;
    color: #c8cacb;
    font-weight: 600;
  }
  .person { margin-top: 42px; }
  .person-name { font-size: 15px; font-weight: 600; color: var(--slate-dark); }
  .person-role { font-size: 14px; color: var(--ink); margin-top: 1px; }
  .contact { margin-top: 14px; font-size: 10.5px; color: var(--ink); }
  .contact-row { display: flex; align-items: center; gap: 18px; margin-top: 4px; white-space: nowrap; }
  .contact-item { display: flex; align-items: center; gap: 5px; }
  .icon { width: 10px; height: 10px; fill: var(--slate); flex: none; }

  .card-back {
    background: var(--sky-soft);
    display: flex;
    align-items: center;
    justify-content: center;
  }
  .card-back .brand-name { font-size: 40px; color: var(--slate); }
  .card-back .brand-dot { width: 26px; height: 26px; background: var(--slate); }
</style>
</head>
<body>

  <section class="card card-front" aria-label="Business card front">
    <svg class="sweep" viewBox="0 0 525 300" preserveAspectRatio="none" aria-hidden="true">
      <path d="M0 0 H372 C502 70 506 232 402 300 H0 Z" fill="#ffffff"/>
      <path d="M0 0 H366 C494 70 498 228 390 300 H0 Z" fill="#878c8c"/>
      <path d="M0 0 H360 C482 40 492 182 368 300 H0 Z" fill="#ffffff"/>
    </svg>

    <div class="front-content">
      <div class="brand">
        <span class="brand-name">The Merry Hound</span>
        <span class="brand-dot"></span>
      </div>
      <p class="tagline">POSITIVE TRAINING SPECIALIST</p>

      <div class="person">
        <p class="person-name">Miriam Caslett</p>
        <p class="person-role">Consultant</p>
      </div>

      <div class="contact">
        <p class="contact-row">041.2nd floor,Harbour Bay Road CRN</p>
        <p class="contact-row">
          <span class="contact-item">
            <svg class="icon" viewBox="0 0 10 10"><path d="M2 0.5 L3.6 2.6 L2.8 3.6 C3.4 5 4.8 6.4 6.2 7 L7.2 6.2 L9.3 7.8 L8 9.5 C4 9 0.9 5.8 0.5 1.8 Z"/></svg>
            0499 731 628
          </span>
          <span class="contact-item">
            <svg class="icon" viewBox="0 0 10 10"><path d="M0.5 2 H9.5 V8 H0.5 Z M0.5 2 L5 5.4 L9.5 2" fill="none" stroke="#757575" stroke-width="1"/></svg>
            miriam@themerryhound-example.com.au
          </span>
        </p>
        <p class="contact-row">
          <span class="contact-item">
            <svg class="icon" viewBox="0 0 10 10"><path d="M1 3 H9 V9 H1 Z M3 0.5 H7 V3 H3 Z"/></svg>
            0499 731 629
          </span>
          <span class="contact-item">
            <svg class="icon" viewBox="0 0 10 10"><circle cx="5" cy="5" r="4.3" fill="none" stroke="#757575" stroke-width="1"/><path d="M0.7 5 H9.3 M5 0.7 C2.8 3 2.8 7 5 9.3 M5 0.7 C7.2 3 7.2 7 5 9.3" fill="none" stroke="#757575" stroke-width="0.8"/></svg>
            www.themerryhound-example.com.au
          </span>
        </p>
      </div>
    </div>
  </section>

  <section class="card card-back" aria-label="Business card back">
    <div class="brand">
      <span class="brand-name">The Merry Hound</span>
      <span class="brand-dot"></span>
    </div>
  </section>

</body>
</html>
```